Life Coaching and Personal Development Business. Needs Business Card with Logo

We are a Life Coaching and Personal Development Business based in Melbourne, Victoria. We specialise in assisting Individuals who find themselves at cross roads due to career, relationships or just life experiences that are preventing them from having extraordinary lives in happiness, finance or relationships or just being disconnected from a sense of purpose. Our motto is "we help you get there".
Updates

Reason: I am awaiting final concepts from a couple of designers

Reason: Deadline passed so now would like to see more options.

Target Market(s)

Individuals who want to move through the cross roads and who are aware that they require help to do so. They are seeking happy, for filing lives through all aspects career, relationships, family and finance

Industry/Entity Type

Finance

Font styles to use
Script

Requirements
Must have
• logo which is representative of moving forward
Business Name: RV Bright Harbour
ABN: 5836071924

I do not have a preference with colour but I do not want red orange or green

Should not have
• The card must not be to busy.

```html
<!DOCTYPE html>
<html lang="en">
<head>
<meta charset="utf-8">
<title>RV Bright Harbour – Business Card</title>
<link rel="stylesheet" href="https://fonts.googleapis.com/css2?family=Tinos:ital,wght@0,400;1,400&display=swap">
<style>
  :root {
    --page: #ffffff;
    --card-front: #ffffff;
    --card-edge: #e2e2e2;
    --card-shadow: #b8b8b8;
    --brand-blue: #1f4f9a;
    --mark-blue: #1c64a8;
    --back-blue: #004a87;
    --back-mark: #0b5e9e;
    --ink: #111111;
    --white: #ffffff;
  }
  * { margin: 0; padding: 0; box-sizing: border-box; }
  html, body {
    width: 897px; height: 1200px; overflow: hidden;
    background: var(--page);
    font-family: "Tinos", "Times New Roman", serif;
  }
  .sheet { position: relative; width: 897px; height: 1200px; }

  .card-front {
    position: absolute; left: 43px; top: 32px; width: 822px; height: 528px;
    background: var(--card-front);
    border: 1px solid var(--card-edge);
    box-shadow: 6px 6px 0 var(--card-shadow);
  }
  .holder {
    position: absolute; left: 608px; top: 22px;
    font-size: 26px; line-height: 1; color: var(--ink); white-space: nowrap;
  }
  .holder-phone { display: flex; align-items: center; gap: 8px; margin-top: 12px; }
  .holder-phone svg { width: 14px; height: 24px; }

  .brand-mark {
    position: absolute; left: 194px; top: 214px; width: 92px; height: 92px;
    background: var(--mark-blue);
  }
  .brand-divider {
    position: absolute; left: 313px; top: 226px; width: 1px; height: 105px;
    background: var(--ink);
  }
  .brand-name {
    position: absolute; left: 338px; top: 247px;
    font-size: 30px; color: var(--brand-blue); white-space: nowrap;
  }
  .brand-abn {
    position: absolute; left: 338px; top: 290px;
    font-size: 20px; color: var(--ink); white-space: nowrap;
  }

  .card-back {
    position: absolute; left: 42px; top: 620px; width: 821px; height: 527px;
    background: var(--back-blue); color: var(--white); overflow: hidden;
  }
  .back-mark {
    position: absolute; left: 340px; top: 100px; width: 150px; height: 150px;
    background: var(--back-mark); opacity: 0.7;
  }
  .motto {
    position: absolute; left: 0; right: 0; top: 222px; text-align: center;
    font-style: italic; font-size: 62px; line-height: 1.1;
    transform: translateX(0px);
  }
  .contacts {
    position: absolute; left: 0; right: 0; top: 454px;
    text-align: center; font-size: 19px; line-height: 27px;
  }
  .contacts span { display: inline-flex; align-items: center; gap: 8px; }
  .contacts svg { width: 17px; height: 17px; }
</style>
</head>
<body>
<main class="sheet">
  <section class="card-front" aria-label="Card front">
    <div class="holder">
      <p class="holder-name">Clara Whitfield</p>
      <p class="holder-phone">
        <svg viewBox="0 0 14 24" aria-hidden="true">
          <rect x="1" y="1" width="12" height="22" rx="2" fill="none" stroke="#1f4f9a" stroke-width="2"/>
          <rect x="3" y="4" width="8" height="14" fill="#1f4f9a"/>
          <circle cx="7" cy="20.5" r="1" fill="#1f4f9a"/>
        </svg>
        04081 36257
      </p>
    </div>
    <div class="brand-mark" aria-hidden="true"></div>
    <div class="brand-divider"></div>
    <p class="brand-name">RV Bright Harbour</p>
    <p class="brand-abn">ABN: 5836071924</p>
  </section>

  <section class="card-back" aria-label="Card back">
    <div class="back-mark" aria-hidden="true"></div>
    <p class="motto">"We help you get there"</p>
    <div class="contacts">
      <p><span>
        <svg viewBox="0 0 17 17" aria-hidden="true">
          <rect x="1" y="3.5" width="15" height="10" fill="none" stroke="#fff" stroke-width="1.2"/>
          <path d="M1 3.5 L8.5 9.5 L16 3.5 M1 13.5 L6.5 8 M16 13.5 L10.5 8" fill="none" stroke="#fff" stroke-width="1.2"/>
        </svg>
        clara@brightharbour.com.au</span></p>
      <p><span>
        <svg viewBox="0 0 17 17" aria-hidden="true">
          <path d="M8.5 1 C5 1 3 3.5 3 6.2 C3 10 8.5 16 8.5 16 C8.5 16 14 10 14 6.2 C14 3.5 12 1 8.5 1 Z" fill="#fff"/>
          <circle cx="8.5" cy="6.2" r="2.2" fill="#004a87"/>
        </svg>
        P.O. Box 4615, Sandhurst VIC 3288</span></p>
    </div>
  </section>
</main>
</body>
</html>
```